E-commerce solution for the nordic market focusing on Quillmoor brands such as Moon Riders and Snowy drift

We need a responsive solution that easily can be implemented in Trellvo.
The style should be very "Clean", the Products speaks for them self and have a lot of colors and prints.
The Products comes in different styles and colors so we need variants.
We need connected Products such as connections between the backpack and the penholder from Moon Riders etc.
Examples that we like are:
www.pindaru.se
www.kavrile.com
www.murtovi.se
www.tinsyparcel.com (OK design, but disaster in mobile device)

Target Market(s)

Children, their parents and grand parents

Industry/Entity Type

Retail

Number of Pages Required

5+ page

Requirements
Must have
• Startpage with offers, news and categories
• Category page
• Product page
• Special offer page
• Info page
• Cart
Nice to have
• Receipt
• e-mail template (offer, news and receipt)

```html
<!DOCTYPE html>
<html lang="en">
<head>
<meta charset="utf-8">
<title>Retail Store – Mobile Start Page</title>
<link href="https://fonts.googleapis.com/css2?family=Cinzel:wght@400;700&family=Lato:wght@400;700&display=swap" rel="stylesheet">
<style>
:root{
  --canvas:#efe9e2;
  --page:#ffffff;
  --ink:#2e2e2e;
  --ink-soft:#6b6b6b;
  --dark:#2b2b2b;
  --darker:#1f1f1f;
  --band:#e9e9e9;
  --line:#d8d8d8;
  --muted:#9a9a9a;
  --light:#f3f3f3;
  --chip:#d9d9d9;
}
*{box-sizing:border-box;margin:0;padding:0}
html,body{width:1200px;height:4500px;overflow:hidden;background:var(--canvas)}
body{font-family:"Lato",Arial,sans-serif;color:var(--ink)}
.page{width:420px;height:4500px;margin:0 auto;background:var(--page);display:flex;flex-direction:column;overflow:hidden}

.topbar{height:52px;flex:none;background:var(--darker);color:#ddd;display:flex;align-items:center;justify-content:center;gap:16px;font-size:11px;letter-spacing:.5px}
.topbar svg{width:22px;height:14px}
.utility{height:28px;flex:none;background:var(--dark);color:#eee;display:flex;justify-content:space-around;align-items:center;font-size:11px;border-top:1px solid #444}
.utility span{display:flex;align-items:center;gap:6px}
.utility svg{width:12px;height:12px}

.brand-row{height:52px;display:flex;align-items:center;justify-content:space-between;padding:0 14px}
.brand-name{font-family:"Cinzel",Georgia,serif;font-size:22px;font-weight:700;letter-spacing:1px}
.cart-mini{display:flex;align-items:center;gap:8px;font-size:11px;color:var(--ink-soft)}
.cart-mini b{display:inline-block;width:24px;height:24px;background:var(--dark);color:#fff;text-align:center;line-height:24px;font-size:11px}
.search-row{height:44px;display:flex;margin:0 14px;border:1px solid var(--line)}
.search-cat{background:var(--dark);color:#fff;font-size:11px;font-weight:700;letter-spacing:1px;padding:0 12px;display:flex;align-items:center}
.search-input{flex:1;font-size:11px;color:var(--muted);display:flex;align-items:center;padding-left:10px;border-right:1px solid var(--line)}
.search-select{font-size:10px;color:var(--ink-soft);display:flex;align-items:center;padding:0 10px;letter-spacing:.5px}
.search-btn{width:40px;background:var(--dark);display:flex;align-items:center;justify-content:center}

.menu{margin:14px 14px 12px}
.menu-title{height:36px;background:var(--dark);color:#fff;font-size:12px;font-weight:700;letter-spacing:1px;display:flex;align-items:center;padding-left:12px}
.menu li{list-style:none;height:40px;border:1px solid var(--line);border-top:none;display:flex;align-items:center;justify-content:space-between;padding:0 12px;font-size:12px;font-weight:700;letter-spacing:.5px}
.menu li::after{content:"›";color:var(--muted);font-size:16px}

.hero{height:218px;flex:none;position:relative;background:linear-gradient(180deg,#c9d9e8 0%,#e4e6ea 55%,#b9a99a 100%)}
.hero-caption{position:absolute;left:0;right:0;bottom:0;height:30px;background:rgba(255,255,255,.85);display:flex;align-items:center;justify-content:space-between;padding:0 12px;font-size:11px}
.dots{display:flex;gap:5px}
.dots i{width:6px;height:6px;border-radius:50%;background:var(--ink-soft);display:block}

.categories{padding:20px 0;display:flex;flex-direction:column;align-items:center;gap:22px}
.cat-tile{width:260px;height:170px;display:flex;flex-direction:column;align-items:center;justify-content:center;gap:10px;color:#fff;border:3px solid #fff;outline:1px solid var(--line)}
.cat-tile.women{background:linear-gradient(135deg,#5b2a22,#a3563f 60%,#3b1c17)}
.cat-tile.men{background:linear-gradient(135deg,#3a3128,#7a6650 60%,#2b241d)}
.cat-tile.kids{background:linear-gradient(135deg,#4a2c3a,#8a5a4a 50%,#2c2230)}
.cat-tile .label{font-family:"Cinzel",Georgia,serif;font-size:22px;letter-spacing:2px}
.cat-tile .btn{font-size:10px;background:rgba(0,0,0,.6);padding:4px 10px}

.section-head{background:var(--band);height:88px;display:flex;flex-direction:column;align-items:center;justify-content:center;gap:10px}
.section-head h2{font-family:"Cinzel",Georgia,serif;font-size:20px;font-weight:700;letter-spacing:1px}
.section-head .dots i{width:4px;height:4px;background:var(--muted)}

.products{display:flex;justify-content:center;gap:30px;padding:16px 0 18px}
.product{width:160px}
.product .photo{height:230px;border:1px solid var(--line)}
.product .photo.p1{background:linear-gradient(180deg,#f1f1f1,#e7e2df 60%,#d9d2cc)}
.product .photo.p2{background:linear-gradient(180deg,#f3ece6,#e07a3a 50%,#2d3a4c)}
.product .name{font-size:11px;text-align:center;margin-top:8px}
.product .buy{display:flex;justify-content:space-between;align-items:center;margin-top:8px;font-size:11px}
.product .buy b{font-weight:700}
.product .buy span{border:1px solid var(--line);padding:3px 6px;font-size:9px}

.promo{height:240px;flex:none;margin-top:20px;display:flex;border-top:1px solid var(--line);border-bottom:1px solid var(--line)}
.promo-text{width:170px;display:flex;align-items:center;padding-left:22px;font-size:13px;line-height:1.45;font-family:"Cinzel",Georgia,serif;font-weight:700;color:var(--ink-soft)}
.promo-photo{flex:1;background:linear-gradient(90deg,#fff,#f2dfe2 40%,#e9e9ee)}

.brands{display:flex;justify-content:center;gap:30px;padding:14px 0 22px}
.brand-tile{width:160px;height:236px;display:flex;flex-direction:column;align-items:center;justify-content:flex-end;padding-bottom:24px;color:#fff;gap:4px}
.brand-tile.b1{background:linear-gradient(180deg,#8e8a88,#5b5453)}
.brand-tile.b2{background:linear-gradient(180deg,#9a9a9a,#3a3a3a)}
.brand-tile .label{font-family:"Cinzel",Georgia,serif;font-size:22px;font-weight:700;letter-spacing:2px}
.brand-tile small{font-size:10px}

.services{display:grid;grid-template-columns:1fr 1fr;row-gap:44px;padding:44px 30px 46px}
.service{text-align:center}
.service svg{width:40px;height:40px}
.service h3{font-size:12px;font-weight:700;letter-spacing:1px;margin-top:8px}
.service h3 span{font-weight:400}
.service p{font-size:10px;color:var(--ink-soft);margin-top:6px}

.features{padding:0 14px;display:flex;flex-direction:column;gap:14px;margin-bottom:14px}
.feature{height:140px;background:#4a4a4a;color:#fff;display:flex;align-items:center;gap:14px;padding:0 14px}
.feature .icon{width:84px;height:84px;flex:none;display:flex;align-items:center;justify-content:center}
.feature h4{font-family:"Cinzel",Georgia,serif;font-size:14px;margin-bottom:8px}
.feature p{font-size:10px;line-height:1.5;color:#ddd}

.newsletter{margin:0 14px 20px;background:var(--light);border:1px solid var(--line);height:284px;flex:none;padding:24px 22px}
.newsletter h3{font-family:"Cinzel",Georgia,serif;font-size:18px;margin-bottom:14px}
.newsletter p{font-size:11px;line-height:1.6;color:var(--ink-soft);margin-bottom:22px}
.newsletter .field{height:32px;border:1px solid var(--line);background:#fff;font-size:10px;color:var(--muted);display:flex;align-items:center;padding-left:10px;margin-bottom:18px}
.newsletter .signup{display:inline-block;background:var(--dark);color:#fff;font-size:10px;font-weight:700;padding:8px 16px;letter-spacing:1px}

.feature-photo{width:240px;height:227px;margin:22px auto;background:linear-gradient(135deg,#7a4a30,#d9a07a 55%,#f0d6c0)}

.testimonials{height:170px;padding:24px 20px 0;text-align:center;position:relative}
.testimonials .who{font-family:"Cinzel",Georgia,serif;font-size:13px;font-weight:700}
.testimonials p{font-size:11px;line-height:1.6;color:var(--ink-soft);margin:8px 40px}
.testimonials .arrow{position:absolute;top:60px;font-size:26px;color:var(--ink-soft)}
.testimonials .arrow.l{left:20px}.testimonials .arrow.r{right:20px}
.testimonials .dots{justify-content:center;margin-top:8px}
.testimonials .dots i{width:5px;height:5px;background:var(--muted)}

.footer{flex:1;background:var(--dark);color:#ccc;padding:28px 18px 0;display:flex;flex-direction:column}
.footer h5{color:#fff;font-size:12px;font-weight:700;letter-spacing:1px;margin-bottom:12px}
.footer .about{font-size:10.5px;line-height:1.8;margin-bottom:28px}
.footer-cols{display:flex;justify-content:space-between}
.footer-cols ul{list-style:none;font-size:10.5px;line-height:2.4}
.footer-bottom{margin-top:auto;margin-left:-18px;margin-right:-18px;background:var(--darker);height:80px;display:flex;align-items:center;justify-content:space-between;padding:0 18px;font-size:9px}
.social{display:flex;gap:6px}
.social i{width:16px;height:16px;border-radius:50%;background:#ddd;display:block}
.pay{display:flex;gap:5px}
.pay i{width:28px;height:18px;border-radius:2px;background:var(--chip);display:block}
</style>
</head>
<body>
<div class="page">

  <div class="topbar">
    <svg viewBox="0 0 22 14" fill="#ddd"><rect x="0" y="2" width="13" height="8"/><path d="M13 4h5l3 3v3h-8z"/><circle cx="4" cy="11" r="2"/><circle cx="17" cy="11" r="2"/></svg>
    <span>FREE DELIVERY ON ORDERS WORLDWIDE</span><span>Sign In</span>
  </div>

  <div class="utility">
    <span><svg viewBox="0 0 13 13" fill="#eee"><path d="M1 1h6l5 5-6 6-5-5z"/></svg>Offers</span>
    <span><svg viewBox="0 0 13 13" fill="#eee"><path d="M6.5 12 1 6.5A3 3 0 0 1 6.5 2.5 3 3 0 0 1 12 6.5z"/></svg>Wishlist</span>
    <span><svg viewBox="0 0 13 13" fill="#eee"><path d="M0 1h2l2 7h7l2-5H4" stroke="#eee" fill="none"/><circle cx="5" cy="11" r="1.3"/><circle cx="10" cy="11" r="1.3"/></svg>Cart</span>
    <span><svg viewBox="0 0 13 13" fill="#eee"><circle cx="6.5" cy="4" r="3"/><path d="M1 13a5.5 5 0 0 1 11 0z"/></svg>My Account</span>
  </div>

  <header>
    <div class="brand-row">
      <div class="brand-name">RETAIL STORE</div>
      <div class="cart-mini">My Cart: 0 items <b>0</b></div>
    </div>
    <div class="search-row">
      <div class="search-cat">CATEGORY ▾</div>
      <div class="search-input">Search</div>
      <div class="search-select">SELECT CATEGORY ▾</div>
      <div class="search-btn"><svg width="16" height="16" viewBox="0 0 16 16" fill="none" stroke="#fff" stroke-width="2"><circle cx="7" cy="7" r="5"/><path d="M11 11l4 4"/></svg></div>
    </div>
  </header>

  <nav class="menu">
    <div class="menu-title">SHOP BY CATEGORY</div>
    <ul>
      <li>WOMEN</li><li>MEN</li><li>KIDS</li><li>SHOES &amp; BAGS</li><li>ACCESSORIES</li>
    </ul>
  </nav>

  <section class="hero" role="img" aria-label="Hero photo of two young women in casual summer outfits">
    <div class="hero-caption"><span>Lorem ipsum dolor sit amet, consectetuer adipis</span><span class="dots"><i></i><i></i><i></i><i></i></span></div>
  </section>

  <section class="categories">
    <div class="cat-tile women" role="img" aria-label="Women category photo"><span class="label">WOMEN</span><span class="btn">Shop Now</span></div>
    <div class="cat-tile men" role="img" aria-label="Men category photo"><span class="label">MEN</span><span class="btn">Shop Now</span></div>
    <div class="cat-tile kids" role="img" aria-label="Kids category photo"><span class="label">KIDS</span><span class="btn">Shop Now</span></div>
  </section>

  <section>
    <div class="section-head"><h2>NEW PRODUCTS</h2><span class="dots"><i></i><i></i><i></i></span></div>
    <div class="products">
      <div class="product">
        <div class="photo p1" role="img" aria-label="Product photo of a white evening dress"></div>
        <div class="name">Womens Evening Dresses</div>
        <div class="buy"><b>$32.00</b><span>Add to Cart</span></div>
      </div>
      <div class="product">
        <div class="photo p2" role="img" aria-label="Product photo of an orange maxi dress"></div>
        <div class="name">Womens Maxi Dresses</div>
        <div class="buy"><b>$32.00</b><span>Add to Cart</span></div>
      </div>
    </div>
  </section>

  <section class="promo">
    <div class="promo-text">SHOP THE LATEST LOOKS IN JULY AT THE LOWEST PRICE</div>
    <div class="promo-photo" role="img" aria-label="Photo of two women in light summer fashion"></div>
  </section>

  <section>
    <div class="section-head"><h2>TOP BRANDS</h2><span class="dots"><i></i><i></i><i></i></span></div>
    <div class="brands">
      <div class="brand-tile b1" role="img" aria-label="Brand photo of two women"><span class="label">LOREM</span><small>Lorem ipsum dolor</small></div>
      <div class="brand-tile b2" role="img" aria-label="Brand photo of a man in a suit"><span class="label">LOREM</span><small>Lorem ipsum dolor</small></div>
    </div>
  </section>

  <section>
    <div class="section-head"><h2>OUR SERVICES</h2><span class="dots"><i></i><i></i><i></i></span></div>
    <div class="services">
      <div class="service">
        <svg viewBox="0 0 40 40" fill="var(--dark)"><path d="M4 22l14-4 8-14h4l-4 13 10-2 3-5h3l-2 8 2 8h-3l-3-5-10-2 4 13h-4l-8-14-14-4z"/></svg>
        <h3>FREE <span>DELIVERY</span></h3><p>Orders above $99</p>
      </div>
      <div class="service">
        <svg viewBox="0 0 40 40" fill="none" stroke="var(--dark)" stroke-width="4"><path d="M30 14a12 12 0 1 0 2 12"/><path d="M30 4v10H20"/></svg>
        <h3>EASY <span>RETURNS</span></h3><p>30 days free returns</p>
      </div>
      <div class="service">
        <svg viewBox="0 0 40 40" fill="var(--dark)"><rect x="6" y="14" width="28" height="8"/><rect x="8" y="22" width="24" height="14"/><rect x="18" y="14" width="4" height="22" fill="#fff"/><path d="M20 14c-6-10-12-4-6 0zM20 14c6-10 12-4 6 0z"/></svg>
        <h3>+500 <span>REWARDS</span></h3><p>Earn points on orders</p>
      </div>
      <div class="service">
        <svg viewBox="0 0 40 40" fill="var(--dark)"><path d="M10 4l7 2 1 8-5 3a22 22 0 0 0 10 10l3-5 8 1 2 7-4 4C17 34 6 23 6 8z"/></svg>
        <h3>CUSTOMER <span>SERVICE</span></h3><p>+00 123 456 789</p><p>Mon–Fri 9–18</p>
      </div>
    </div>
  </section>

  <section class="features">
    <div class="feature">
      <div class="icon"><svg viewBox="0 0 84 60" width="84" height="60" fill="#fff"><rect x="0" y="6" width="52" height="38"/><path d="M54 18h16l12 14v12H54z"/><circle cx="14" cy="48" r="8" fill="#4a4a4a" stroke="#fff" stroke-width="3"/><circle cx="66" cy="48" r="8" fill="#4a4a4a" stroke="#fff" stroke-width="3"/><text x="26" y="32" text-anchor="middle" font-family="Lato,Arial,sans-serif" font-weight="700" font-size="15" fill="#4a4a4a">FREE</text></svg></div>
      <div><h4>FREE SHIPPING WORLDWIDE</h4><p>Lorem ipsum dolor sit amet, consectetur adip elit, sed do eiusmod tempor incididunt ut labore.</p></div>
    </div>
    <div class="feature">
      <div class="icon"><svg viewBox="0 0 84 84" width="80" height="80"><circle cx="42" cy="42" r="38" fill="#ddd"/><circle cx="42" cy="42" r="28" fill="#4a4a4a"/></svg></div>
      <div><h4>MONEY BACK GUARANTEE</h4><p>Lorem ipsum dolor sit amet, consectetur adip elit, sed do eiusmod tempor incididunt ut labore.</p></div>
    </div>
  </section>

  <section class="newsletter">
    <h3>Subscribe To Our Newsletter</h3>
    <p>Subscribe to our Newsletter and we will send you news and information about new brands every week.</p>
    <div class="field">Your Email Address</div>
    <span class="signup">SIGNUP</span>
  </section>

  <section>
    <div class="section-head"><h2>NEW PRODUCTS</h2><span class="dots"><i></i><i></i><i></i></span></div>
    <div class="feature-photo" role="img" aria-label="Portrait photo of a smiling woman"></div>
  </section>

  <section>
    <div class="section-head"><h2>OUR CUSTOMERS ARE SAYING</h2><span class="dots"><i></i><i></i><i></i></span></div>
    <div class="testimonials">
      <div class="who">RETAIL STORE</div>
      <p>Lorem ipsum dolor sit amet, consectetur adipiscing elit, sed do eiusmod tempor incididunt ut labore et dolore.</p>
      <p>— Jane, Customer</p>
      <span class="arrow l">‹</span><span class="arrow r">›</span>
      <div class="dots"><i></i><i></i><i></i><i></i></div>
    </div>
  </section>

  <footer class="footer">
    <h5>ABOUT RETAIL STORE</h5>
    <p class="about">Lorem ipsum dolor sit amet, consectetur adipiscing elit. Integer nec odio praesent libero sed cursus ante dapibus diam. Sed nisi nulla quis sem at nibh elementum imperdiet. Duis sagittis ipsum praesent mauris fusce nec tellus sed augue semper porta mauris massa vestibulum lacinia arcu eget nulla.</p>
    <div class="footer-cols">
      <div><h5>QUICK LINKS</h5><ul><li>Home</li><li>New In</li><li>Women</li><li>Men</li><li>Kids</li></ul></div>
      <div><h5>CUSTOMER SERVICE</h5><ul><li>Help</li><li>Shipping</li><li>Returns</li><li>Contact Us</li><li>Privacy</li></ul></div>
      <div><h5>KEEP UP WITH US</h5><ul><li>Newsletter</li><li>Blog</li><li>Events</li><li>Careers</li></ul></div>
    </div>
    <div class="footer-bottom">
      <span class="social"><i></i><i></i><i></i><i></i></span>
      <span>© 2024 Retail Store. All rights reserved.</span>
      <span class="pay" aria-label="Accepted payment methods"><i></i><i></i><i></i><i></i></span>
    </div>
  </footer>

</div>
</body>
</html>
```